The Harlow Reserve Web Site design

I need a web design for my luxury range of Terry Toweling and Spa Accessories for luxury upmarket hotels and Spas. I have a catalog that sets the mood and tone I am looking for. I need a website design that shows off the look and feel of this luxury range while working back to the catalog look and feel. Its all about Upmarket and Luxury. I will be using the website as a reference site and as a site that customers can purchase off.
The Logo is attached as is the catalog. I don't mind changing the color of the Logo to match the website. However I would prefer to keep the font of that logo.

http://thegalleryloft.pixvaultex.com/p204519873
Please can you try and access this link. The Harlow Reserve
Name Bettina. Email bettina@kestrelsupplyco.com.au. Password Harlow.
These images are to be used for shopping page and please use the close up details of texture as background on pages and use those texture details and close ups for banners

Please note the look and feel has to be very upmarket and super luxury. Ficus is on mood and not on retail.
Have a look at the mood on the following websites
Www.gracefulretreatsex.com
And ourquietcovecottagestore.com
That one is retail .mi don't want retail focus but it's very clean. And simple and colors are good

Please rebook brief. I have added some important detail. Thanks

Relook brief. I have added,important detail. Thanks

Target Market(s)

Corporate buyers
This is not for retail selling to consumers
Price it's viewed only after secure login

Industry/Entity Type

Shopping

Colors
acd037
cadf82
fbc995
fce7d3
faa54b

Requirements
Must have
• Luxury. Think luxury. Very high end yet modern like the catalogue
Use banners on home page
Should not have
• Don't use the blue as the main color. It's too cheap.
No products on home page

```html
<!DOCTYPE html>
<html lang="en">
<head>
<meta charset="utf-8">
<title>The Harlow Reserve</title>
<link href="https://fonts.googleapis.com/css2?family=Lobster&family=Open+Sans:wght@400;600&family=Libre+Baskerville&family=Arimo:wght@400;700&display=swap" rel="stylesheet">
<style>
:root{
  --green:#acd037;
  --green-soft:#cadf82;
  --peach:#fbc995;
  --cream:#fce7d3;
  --orange:#faa54b;
  --dark:#1c1c1c;
  --tile-dark:#3d3d3d;
  --ink:#222;
  --footer-ink:#5a3410;
  --white:#fff;
}
*{box-sizing:border-box;margin:0;padding:0}
html,body{width:1063px;height:1200px;overflow:hidden}
body{position:relative;background:var(--white);font-family:"Arimo",Arial,sans-serif;color:var(--ink)}
.abs{position:absolute}

.topbar{left:0;top:0;width:1063px;height:31px;background:var(--cream)}
.topbar .call{left:147px;top:8px;font:600 13px "Open Sans",sans-serif;color:#333;display:flex;align-items:center;gap:4px}
.topbar .account{right:156px;top:8px;font:400 11px "Open Sans",sans-serif;color:#333;letter-spacing:.5px;display:flex;gap:14px}

.header{left:0;top:31px;width:1063px;height:86px;background:var(--white)}
.brand{left:160px;top:22px;font:38px "Lobster",cursive;color:var(--orange)}
.header-icon{top:33px;width:32px;height:32px;border-radius:50%}
.header-icon.search{left:837px;background:var(--orange)}
.header-icon.cart{left:875px;background:var(--green)}
.header-icon svg{display:block;margin:8px}

.nav{left:0;top:117px;width:1063px;height:31px;background:var(--peach)}
.nav a{position:absolute;top:0;height:31px;line-height:31px;font:400 14px/31px "Open Sans",sans-serif;color:#222;text-decoration:none}
.nav a.active{background:var(--green);padding:0 21px}

.hero{left:0;top:148px;width:1063px;height:313px;background:linear-gradient(100deg,#cfcfcf 0%,#a9a9a6 35%,#7d7a6a 55%,#6f7d52 75%,#94a97a 100%)}
.hero-caption{left:218px;top:123px;width:644px;height:75px;background:rgba(60,60,60,.35);font:24px/30px "Libre Baskerville",serif;color:var(--white);text-align:center;padding-top:8px}
.hero-arrow{top:138px;width:37px;height:37px;border-radius:50%;background:rgba(255,255,255,.85)}
.hero-arrow svg{display:block;margin:11px}

.categories{left:0;top:461px;width:1063px;height:356px;background:var(--dark)}
.tile{position:absolute;height:145px}
.tile.photo{}
.tile.text{padding:16px 17px}
.tile.text.green{background:var(--green)}
.tile.text.charcoal{background:var(--tile-dark)}
.tile.text.orange{background:var(--orange)}
.tile h3{font:400 24px "Lobster",cursive;color:var(--white);margin-bottom:8px}
.tile p{font:12.5px/15px "Arimo",Arial,sans-serif;color:var(--white)}
.tile .more{position:absolute;right:16px;bottom:16px}

.intro{left:0;top:817px;width:1063px;height:210px}
.intro h2{position:absolute;font:400 16px "Open Sans",sans-serif;color:var(--orange)}
.intro p{position:absolute;font:11px/14.2px "Arimo",Arial,sans-serif;color:#111}
.btn-read{left:156px;top:144px;width:72px;height:19px;background:var(--green);color:var(--white);font:600 11px/19px "Open Sans",sans-serif;text-align:center}
.pdf-button{left:415px;top:109px}
.promo{left:664px;top:34px;width:243px;height:129px;border:4px solid #c8c8c8;background:linear-gradient(180deg,#8c7a5e 0%,#a3927a 40%,#e8e6e2 75%,#f4f3f1 100%)}
.promo .label{position:absolute;left:4px;right:4px;bottom:2px;height:20px;background:var(--green);color:var(--white);font:700 12.5px/20px "Arimo",Arial,sans-serif;text-align:center}

.footer{left:0;top:1027px;width:1063px;height:149px;background:var(--orange)}
.footer h4{position:absolute;top:9px;font:700 12px "Arimo",Arial,sans-serif;color:var(--white)}
.footer ul{position:absolute;top:30px;list-style:none;font:10.5px/14.4px "Arimo",Arial,sans-serif;color:var(--footer-ink)}
.footer .note{position:absolute;font:10.5px/14px "Arimo",Arial,sans-serif;color:var(--footer-ink)}
.footer .email-field{left:402px;top:71px;width:124px;height:18px;background:var(--white);border:1px solid #d9d9d9;font:italic 10px/16px "Arimo",Arial,sans-serif;color:#555;padding-left:6px}
.footer .submit{left:402px;top:102px;width:63px;height:19px;background:var(--green);color:var(--white);font:700 12px/19px "Arimo",Arial,sans-serif;text-align:center}
.contact-row{position:absolute;left:561px;font:10.5px/14px "Arimo",Arial,sans-serif;color:var(--footer-ink);display:flex;gap:6px}
.contact-row b{color:var(--white);font-weight:700}
.social{left:776px;top:31px;display:flex;gap:5px}
.social span{width:20px;height:20px;border-radius:50%;background:#1f2a44}
.payments{left:775px;top:61px;width:110px;height:69px;background:var(--white)}

.copyright{left:0;top:1176px;width:1063px;height:24px;background:#1a1a1a;color:var(--white);font:11px/24px "Arimo",Arial,sans-serif;text-align:center}
</style>
</head>
<body>

<div class="abs topbar">
  <div class="abs call">
    <svg width="12" height="12" viewBox="0 0 24 24"><path fill="#333" d="M6.6 10.8a15.1 15.1 0 0 0 6.6 6.6l2.2-2.2c.3-.3.7-.4 1-.2 1.1.4 2.3.6 3.6.6.6 0 1 .4 1 1V20c0 .6-.4 1-1 1A17 17 0 0 1 3 4c0-.6.4-1 1-1h3.5c.6 0 1 .4 1 1 0 1.3.2 2.5.6 3.6.1.3 0 .7-.2 1z"/></svg>
    Call to Order: 1-877-555-0148
  </div>
  <div class="abs account"><span>Registration</span><span>Log In</span></div>
</div>

<header class="abs header">
  <div class="abs brand">The Harlow Reserve</div>
  <div class="abs header-icon search">
    <svg width="16" height="16" viewBox="0 0 16 16"><circle cx="6.5" cy="6.5" r="4.5" fill="none" stroke="#fff" stroke-width="2"/><path d="M10 10l4 4" stroke="#fff" stroke-width="2.4" stroke-linecap="round"/></svg>
  </div>
  <div class="abs header-icon cart">
    <svg width="16" height="16" viewBox="0 0 16 16"><path d="M1 2h2.5l1.6 8h7.6l1.6-6H4.2" fill="none" stroke="#fff" stroke-width="1.6" stroke-linejoin="round"/><path d="M4.5 4h9.8l-1.6 6H5.1z" fill="#fff"/><circle cx="6" cy="13.2" r="1.4" fill="#fff"/><circle cx="12" cy="13.2" r="1.4" fill="#fff"/></svg>
  </div>
</header>

<nav class="abs nav">
  <a class="active" style="left:148px">Home</a>
  <a style="left:258px">About Us</a>
  <a style="left:366px">Products</a>
  <a style="left:473px">New Collection</a>
  <a style="left:613px">Accessories</a>
  <a style="left:736px">Contact Us</a>
</nav>

<section class="abs hero" role="img" aria-label="Spa guest resting on a massage table under a white textured towel, with green leaves behind">
  <div class="abs hero-caption">The Harlow Reserve Allows You To Transform Your<br>Bathroom, Spa, Or Poolside Into A True Retreat.</div>
  <div class="abs hero-arrow" style="left:156px"><svg width="15" height="15" viewBox="0 0 15 15"><path d="M9.5 3L5 7.5 9.5 12" fill="none" stroke="#222" stroke-width="2"/></svg></div>
  <div class="abs hero-arrow" style="left:869px"><svg width="15" height="15" viewBox="0 0 15 15"><path d="M5.5 3L10 7.5 5.5 12" fill="none" stroke="#222" stroke-width="2"/></svg></div>
</section>

<section class="abs categories">
  <div class="tile photo" style="left:156px;top:35px;width:174px;background:linear-gradient(180deg,#8fb0c8 0%,#4f7a3e 35%,#5f7d74 60%,#c9c4b4 85%,#a9a296 100%)" role="img" aria-label="White massage table set up by the water with palm trees"></div>
  <div class="tile text green" style="left:330px;top:35px;width:201px">
    <h3>Spa Accessories</h3>
    <p>Lorem ipsum dolor sit amet consectetuer adipiscing elit sed diam nonummy nibh euismod</p>
    <svg class="more" width="25" height="25" viewBox="0 0 25 25"><circle cx="12.5" cy="12.5" r="11.3" fill="none" stroke="#fff" stroke-width="1.6"/><path d="M10.5 7.5l5 5-5 5" fill="none" stroke="#fff" stroke-width="2"/></svg>
  </div>
  <div class="tile photo" style="left:531px;top:35px;width:175px;background:linear-gradient(135deg,#4c5a3e 0%,#3a4150 40%,#5b5d6a 60%,#3b2a24 85%,#2a1e1a 100%)" role="img" aria-label="Folded textured fabric swatches in olive, slate and brown"></div>
  <div class="tile text charcoal" style="left:706px;top:35px;width:201px">
    <h3>New Collection</h3>
    <p>Lorem ipsum dolor sit amet consectetuer adipiscing elit sed diam nonummy nibh euismod</p>
    <svg class="more" width="25" height="25" viewBox="0 0 25 25"><circle cx="12.5" cy="12.5" r="11.3" fill="none" stroke="#fff" stroke-width="1.6"/><path d="M10.5 7.5l5 5-5 5" fill="none" stroke="#fff" stroke-width="2"/></svg>
  </div>

  <div class="tile text charcoal" style="left:156px;top:179px;width:201px">
    <h3>Terry Towels</h3>
    <p>Lorem ipsum dolor sit amet consectetuer adipiscing elit sed diam nonummy nibh euismod</p>
    <svg class="more" width="25" height="25" viewBox="0 0 25 25"><circle cx="12.5" cy="12.5" r="11.3" fill="none" stroke="#fff" stroke-width="1.6"/><path d="M10.5 7.5l5 5-5 5" fill="none" stroke="#fff" stroke-width="2"/></svg>
  </div>
  <div class="tile photo" style="left:357px;top:179px;width:174px;background:linear-gradient(180deg,#e0473a 0%,#d8564a 25%,#3d4a55 45%,#324050 55%,#f08a3a 72%,#f25a1e 100%)" role="img" aria-label="Stack of folded terry towels in red, navy and orange"></div>
  <div class="tile text orange" style="left:531px;top:179px;width:202px">
    <h3>Throws</h3>
    <p>Lorem ipsum dolor sit amet consectetuer adipiscing elit sed diam nonummy nibh euismod</p>
    <svg class="more" width="25" height="25" viewBox="0 0 25 25"><circle cx="12.5" cy="12.5" r="11.3" fill="none" stroke="#fff" stroke-width="1.6"/><path d="M10.5 7.5l5 5-5 5" fill="none" stroke="#fff" stroke-width="2"/></svg>
  </div>
  <div class="tile photo" style="left:733px;top:179px;width:174px;background:linear-gradient(160deg,#e6e4e0 0%,#8ec6c8 30%,#efece6 50%,#c44a4a 70%,#e9e6e2 100%)" role="img" aria-label="Striped throws in teal, red and cream hanging on a rail"></div>
</section>

<section class="abs intro">
  <h2 style="left:156px;top:32px">About Us</h2>
  <p style="left:156px;top:62px;width:216px">Lorem ipsum dolor sit amet, consectetuer adipiscing elit, sed diam nonummy nreibh euismod tincidunt ut laoreet dolore magna aliquam erat volutpat. Ut wisi enim ad min veniam, quis nostrud exerci tation ullam</p>
  <div class="abs btn-read">Read More</div>

  <h2 style="left:413px;top:32px">Download Our Brochure</h2>
  <p style="left:417px;top:62px;width:220px">Lorem ipsum dolor sit amet, consectetuer adipiscing elit sed diam non</p>
  <svg class="abs pdf-button" width="230" height="56" viewBox="0 0 230 56">
    <defs><linearGradient id="pdfRed" x1="0" y1="0" x2="0" y2="1"><stop offset="0" stop-color="#e53a3a"/><stop offset=".5" stop-color="#d11f1f"/><stop offset="1" stop-color="#a80f0f"/></linearGradient></defs>
    <rect x="36" y="12" width="191" height="38" rx="6" fill="url(#pdfRed)"/>
    <text x="130" y="38" text-anchor="middle" font-family="Arimo, Arial, sans-serif" font-weight="700" font-size="20" fill="#fff">Download PDF</text>
    <path d="M2 1h28l8 8v45H2z" fill="#f4f4f4" stroke="#9a9a9a"/>
    <path d="M30 1v8h8" fill="#ddd" stroke="#9a9a9a"/>
    <rect x="0" y="6" width="24" height="11" fill="#d11f1f"/>
    <text x="12" y="15" text-anchor="middle" font-family="Arimo, Arial, sans-serif" font-weight="700" font-size="8.5" fill="#fff">PDF</text>
  </svg>

  <div class="abs promo" role="img" aria-label="Stack of folded white towels on a brown background">
    <div class="label">20% Off On First Purchase.....Hurry</div>
  </div>
</section>

<footer class="abs footer">
  <h4 style="left:158px">Quick Links</h4>
  <ul style="left:158px"><li>Home</li><li>About Us</li><li>Products</li><li>New Collection</li><li>Accessories</li><li>Contact Us</li></ul>

  <h4 style="left:268px">Service &amp; Support</h4>
  <ul style="left:268px"><li>My Account</li><li>Terms &amp; Conditions</li><li>Buying Guide</li><li>Shipping Details</li><li>FAQ's</li><li>My Cart</li><li>Terms of Use</li></ul>

  <h4 style="left:401px">Newsletter SignUp</h4>
  <div class="note" style="left:402px;top:31px">Join Our newsletter list<br>to get the latest updates</div>
  <div class="abs email-field">email address</div>
  <div class="abs submit">Submit</div>

  <h4 style="left:561px">Contact Information</h4>
  <div class="contact-row" style="top:31px"><b>A:</b><span>Street Name, City Name<br>State Zip Code</span></div>
  <div class="contact-row" style="top:68px"><b>P:</b><span>123-555-0190</span></div>
  <div class="contact-row" style="top:91px"><b>F:</b><span>456-555-0127</span></div>
  <div class="contact-row" style="top:114px"><b>E:</b><span>Support@harlowreserve.com</span></div>

  <h4 style="left:776px">Follow Us On</h4>
  <div class="abs social"><span style="background:var(--green)"></span><span></span><span></span><span></span><span></span></div>
  <svg class="abs payments" width="110" height="69" viewBox="0 0 110 69">
    <rect x="6" y="6" width="98" height="28" fill="none" stroke="var(--orange)"/>
    <rect x="12" y="18" width="19" height="12" fill="#d9d9d9"/><rect x="34" y="18" width="19" height="12" fill="#d9d9d9"/><rect x="56" y="18" width="19" height="12" fill="#d9d9d9"/><rect x="78" y="18" width="19" height="12" fill="#d9d9d9"/>
    <rect x="6" y="38" width="98" height="26" fill="none" stroke="#bbb"/>
    <rect x="12" y="50" width="19" height="10" fill="#d9d9d9"/><rect x="34" y="50" width="19" height="10" fill="#d9d9d9"/><rect x="56" y="50" width="19" height="10" fill="#d9d9d9"/><rect x="78" y="50" width="19" height="10" fill="#d9d9d9"/>
  </svg>
</footer>

<div class="abs copyright">©2014 TheHarlowReserve All Rights Reserved</div>

</body>
</html>
```